Professional WordPress Website Design & Development for IT Consulting Company (Trelvo)

We are an IT consulting company (Trelvo) based in Germany and are looking for a professional, modern and scalable WordPress website design INCLUDING full coding (WordPress theme/template).

IMPORTANT:
We do NOT want only a design (eg Photoshop files).
We want a fully working, coded WordPress website that we can host and manage ourselves.

The uploaded files (PowerPoint, HTML, logo) are ONLY for rough orientation.
They do NOT represent the final structure but give an idea of our visual style.

---

## COMPANY STRUCTURE (IMPORTANT)

Currently we operate as:

* Trelvo UG (limited liability)

Planned structure:

* Trelvo Operations GmbH (main operating company)
* Trelvo Holding GmbH
* optionally later: Trelvo Capital GmbH

The website should be designed as a scalable group website, but currently focus on the main brand "Trelvo".

---

## BUSINESS FOCUS (IMPORTANT)

Our main business is:
→ Managed Services (core focus)

Additional areas:

* IT Infrastructure (Nexorin, Valtek, Quadr-X)
* Windows Server/Client environments
* Cloud & Hybrid solutions
* Network, Firewall, VPN
* Data center operations, migrations and rollouts

The website should clearly communicate:
→ reliability, scalability, enterprise-level service quality

---

## DESIGN STYLE & VISUAL DIRECTION

We like the design direction from our uploaded PowerPoint.

IMPORTANT:

* We especially like the green checkered/grid-style background with dark/black gradient
* This style should be used as inspiration
* Colors: green + dark/black + modern IT style

Design should be:

* modern
* clean
* professional
* enterprise-level
* trustworthy
* not playful or overloaded

---

## TECHNICAL REQUIREMENTS

* WordPress (self-hosted)
* Full source code delivery (no proprietary lock-in)
* Custom theme or clean reusable theme
* Editable without developer
* Multilingual: German, English, Polish
* SEO-friendly
* Fast performance
* GDPR/DSVO compliant contact form

---

## RESPONSIVE DESIGN & ACCESSIBILITY

Must be optimized for:

* Desktop
* Tablet
* Mobile

Layout must adapt automatically.

Accessibility:

* Clear typography
* Good contrast
* Easy navigation
* Mobile-friendly usability

Mobile experience must be fully functional and professional.

---

## STRUCTURE (NO ONE-PAGE WEBSITE)

We want a structured website with pages and subpages.

MAIN NAVIGATION (HEADER):

* Home
* Managed Services (MAIN FOCUS)
* Services
* Solutions / Expertise
* Projects / News
* Resources
* Careers
* Company
* Contact

SUBNAVIGATION / SUBPAGES (examples):

Managed Services:

* Overview
* Service Models
* SLAs & Support
* Monitoring & Operations

Services:

* Nexorin
* Valtek
* Quadr-X
* Windows Server / Client
* PLDM / Ombrex
* Network / Firewall / VPN

Solutions:

* Data Center
* Cloud / Hybrid
* Migration Projects
* Security / Zero Trust

Projects / News:

* Projects
* Opportunities
* Articles

Resources:

* Available Experts
* Freelancer / Partner
* Internal Staff

Careers:

* Open Positions
* Freelancer Opportunities

Company:

* About Us
* Group Structure
* Values
* References

---

## HEADER / FOOTER STRUCTURE

HEADER:

* Sticky header (always visible)
* Main navigation with dropdowns or mega menu
* Clean, structured layout

FOOTER:

* Legal pages (Imprint, Privacy, Terms)
* Contact information
* Possibly quick links
* Consistent across all pages

---

## SPECIAL FEATURES

1. PROJECT / NEWS SYSTEM

* publish projects
* project opportunities
* articles

2. RESOURCE SYSTEM

* freelancers
* partners
* internal staff

With:

* skills
* availability
* role
* location
* language

---

## IMAGES, ICONS & LICENSING

Stock images (eg picVault) may be used as placeholders.

IMPORTANT:

* We will purchase final licenses ourselves
* No Zerlin images or unknown sources

Icons and illustrations are welcome but must be properly licensed.

At delivery:

* Full asset list required (images, icons, sources, licenses)

---

## DELIVERABLES

We expect:

* Fully working WordPress website
* Full source code
* Installation instructions
* Plugin list
* No hidden dependencies
* No forced subscriptions
* Full usage rights

---

## IMPORTANT

We want to pay ONCE and fully own everything.

---

## LANGUAGES

Content will be managed by us:

* German
* English
* Polish

---

## FILES

Uploaded files are only for inspiration.

---

We are looking for a long-term, scalable and professional solution suitable for enterprise customers.
Updates

Additional update regarding interactions, hover effects and animations:

HOVER EFFECTS

We would like to include subtle and modern hover effects across the website:

Cards (eg Open Positions, Projects): → slight green glow on hover → minimal lift effect (approx. 2–4px)

Navigation (header): → hover color should be green (NOT orange)

Footer links (Imprint, Privacy, Terms): → slightly brighter on hover

Social icons (Brumble, FLOB, Gigharborly): → subtle glow and slight scale on hover

IMPORTANT: All hover effects must be consistent, clean and not exaggerated.

ACTIVE STATE (VERY IMPORTANT)

Navigation elements must clearly show when they are active (current page).

This applies to:

Header navigation footer left

Behavior:

Active links should remain highlighted (eg green color and/or subtle underline) Users should always clearly see which page they are currently on

IMPORTANT: Active and hover states must be visually consistent across the entire website.

ANIMATIONS / MICRO INTERACTIONS

The website should not feel static.

We would like subtle and professional animations, such as:

smooth transitions between elements minimal background movement (very subtle) soft UI interactions

IMPORTANT: No heavy, flashy or distracting animations.

The goal is a high-end, enterprise-level feel.

COUNTERS / KEY METRICS

We want animated key numbers, for example:

150+ clients 10+ years experience 24/7 support 99.9% uptime

Behavior:

numbers should count up when they come into view (on scroll) fast and smoothly (approx. 0. 5–1 seconds) animation should trigger only once

Overall goal: A modern, dynamic and high-quality website with subtle interactions, not a flashy or overloaded design.

Hi everyone,

I have uploaded additional reference files to give you a clearer idea of the direction we are aiming for.

IMPORTANT: These files are only meant as inspiration and guidance – they are NOT strict templates that must be copied 1:1.

What we particularly like:

Dark / black + green design Subtle grid / tech background (as seen in the PowerPoint) Clean, modern and professional enterprise IT style Structured layout (no one-page scrolling) LANGUAGE FLAGS (IMPORTANT UPDATE)

Please adjust the language selection as follows:

Order:

German (DE) English (EN) Polish (PL)

For ENGLISH: We do NOT want a standard flag.

Instead, please create a combined UK/US flag:

Diagonally split design One side showing the UK flag The other side showing the US flag

This should look clean and professional (not playful).

FOOTER (IMPORTANT)

Footer should be:

Minimal and clean (not large or heavy) Positioned at the very bottom

Include:

Legal Notice / Imprint / Privacy Policy / Data Protection / Terms and Conditions / Terms

And: © Trelvo UG

Social icons:

Brumble FLOB Gigharborly

Please remove:

Pawstream Chirply Snapmoor LAYOUT NOTE

Please avoid duplicate sections (eg "About Us" appearing multiple times).

We prefer a clean and structured layout with clear sections.

Thank you very much – looking forward to your designs!

Ich brauche zusätzliche Tage um durchzusehen

Target Market(s)

Enterprise and mid-sized companies, especially in automotive, finance, technology and IT infrastructure environments.

Industry/Entity Type

IT Consulting / Managed Services / Enterprise IT

Coding

Coded - Design and coding required

Font styles to use
Sans Serif

Colors
0094D4
00A9DD
6FCCEA
C7EBF8
E9F6FB
00AB8E
00BBA5
67D7C9
C6EFE9
E9F9F6
59FF00
82FF00
B8FF75
E3FFCB
F4FFEA

Requirements
Must have
• - Fully coded WordPress website (not just design) - Self-hosted, no dependency on designer - Responsive (desktop, tablet, mobile) - Multilingual (German, English, Polish) - Editable without developer - Clean, modern enterprise design - Structured navigation with subpages (no one-page website) - GDPR-compliant contact form - Scalable structure for future company expansion (group structure)
Nice to have
• - Subtle modern animations (not overloaded) - Mega menu or structured dropdown navigation - Clean icon set and optional illustrations - Reusable page templates - Fast loading performance - SEO-friendly structure - Team presentation with profiles (management, internal staff, technical roles) - Integration of social links (Brumble, Flob, Gigharborly)
Should not have
• - No one-page scrolling website - No overly colorful or playful design - No outdated or generic templates - No confusing or complex navigation - No cheap-looking stock-heavy layouts - No dependency on proprietary builders or subscriptions

```html
<!DOCTYPE html>
<html lang="en">
<head>
<meta charset="utf-8">
<title>Trelvo – Solutions</title>
<link rel="stylesheet" href="https://fonts.googleapis.com/css2?family=Inter:wght@400;500;600&family=Space+Grotesk:wght@500;600&family=JetBrains+Mono:wght@400;500&family=Barlow+Semi+Condensed:wght@700&display=swap">
<style>
:root{
  --bg:#0c0d12;
  --bg-band:#121725;
  --bg-footer:#10131d;
  --card:#0e0f15;
  --line:#1d1f27;
  --text:#f2f3f5;
  --muted:#a3a7b1;
  --dim:#7d818b;
  --green:#82ff00;
  --green-btn:#6fd42a;
  --green-soft:#59c22a;
  --num:#233a1e;
}
*{box-sizing:border-box;margin:0;padding:0}
html,body{width:1200px;height:2713px;overflow:hidden;background:var(--bg);color:var(--text);font-family:"Inter",sans-serif}
a{color:inherit;text-decoration:none}
.grid-bg{background-image:linear-gradient(rgba(255,255,255,.018) 1px,transparent 1px),linear-gradient(90deg,rgba(255,255,255,.018) 1px,transparent 1px);background-size:44px 44px}
.mono{font-family:"JetBrains Mono",monospace}
.eyebrow{font-family:"JetBrains Mono",monospace;font-size:9.5px;letter-spacing:1.2px;color:var(--green);font-weight:500}
.display{font-family:"Barlow Semi Condensed",sans-serif;font-weight:700;text-transform:uppercase;letter-spacing:-.3px;line-height:1}

/* header */
.site-header{position:absolute;top:0;left:0;width:1200px;height:63px;border-bottom:1px solid var(--line);display:flex;align-items:center;padding:0 32px 0 27px}
.brand{display:flex;align-items:center;gap:8px}
.brand-mark{width:12px;height:12px;background:var(--green-soft);border-radius:2px}
.brand-name{font-family:"Space Grotesk",sans-serif;font-weight:600;font-size:22px;color:var(--green-soft)}
.main-nav{position:absolute;left:462px;display:flex;gap:22px;font-family:"JetBrains Mono",monospace;font-size:11px;color:var(--muted);letter-spacing:.5px}
.main-nav .active{color:var(--green);border-bottom:1px solid var(--green);padding-bottom:3px}
.lang{position:absolute;left:1038px;display:flex;align-items:center;gap:5px;font-family:"JetBrains Mono",monospace;font-size:10px;color:var(--muted)}
.btn{display:inline-flex;align-items:center;justify-content:center;gap:6px;background:var(--green-btn);color:#0b0d0a;font-size:11px;font-weight:500;border-radius:7px}
.header-cta{position:absolute;left:1084px;top:11px;width:84px;height:31px}

/* hero */
.hero{position:absolute;top:63px;left:0;width:1200px;height:1076px}
.hero-label{position:absolute;left:84px;top:60px}
.hero-title{position:absolute;left:84px;top:80px;font-size:56px}
.hero-lead{position:absolute;left:84px;top:149px;width:390px;font-size:11.5px;line-height:19px;color:var(--muted)}

.solutions{position:absolute;left:84px;top:318px;width:1028px;display:grid;grid-template-columns:503px 503px;gap:23px 22px}
.solution-card{height:334px;background:var(--card);border:1px solid var(--line);border-radius:12px;padding:28px 28px 0}
.icon-box{width:38px;height:38px;border-radius:9px;background:#1a2317;display:flex;align-items:center;justify-content:center}
.icon-box.cloud{background:#161c25}
.icon-box.swap{background:#2a2116}
.icon-box.shield{background:#2b1717}
.solution-card h3{font-family:"Space Grotesk",sans-serif;font-weight:500;font-size:17px;margin-top:20px}
.solution-card p{font-size:11.5px;line-height:17px;color:var(--muted);margin-top:14px;width:445px}
.checks{list-style:none;margin-top:14px}
.checks li{display:flex;align-items:center;gap:9px;font-size:10px;color:var(--muted);height:22.4px}
.outline-btn{margin-top:12px;height:35px;border:1px solid #262831;border-radius:8px;display:flex;align-items:center;justify-content:center;gap:6px;font-size:11.5px;font-weight:500}

/* approach */
.approach{position:absolute;top:1139px;left:0;width:1200px;height:402px;background:var(--bg-band)}
.approach .eyebrow{position:absolute;top:91px;width:1200px;text-align:center}
.approach h2{position:absolute;top:113px;width:1200px;text-align:center;font-size:40px}
.steps{position:absolute;left:84px;top:196px;display:grid;grid-template-columns:repeat(4,262px)}
.step-num{font-family:"Space Grotesk",sans-serif;font-weight:600;font-size:50px;color:var(--num);line-height:1}
.step h3{font-family:"Space Grotesk",sans-serif;font-weight:500;font-size:13.5px;margin-top:14px}
.step p{font-size:9.5px;line-height:14px;color:var(--muted);margin-top:8px;width:240px}

/* industries */
.industries{position:absolute;top:1541px;left:0;width:1200px;height:540px}
.industries .eyebrow{position:absolute;left:84px;top:128px}
.industries h2{position:absolute;left:84px;top:148px;font-size:40px}
.industries .lead{position:absolute;left:84px;top:203px;width:440px;font-size:11.5px;line-height:19px;color:var(--muted)}
.industry-list{position:absolute;left:84px;top:261px;display:grid;grid-template-columns:240px 240px;gap:12px 12px}
.chip{height:31px;border:1px solid var(--line);border-radius:7px;display:flex;align-items:center;gap:7px;padding-left:10px;font-size:10px;color:#d6d8dc}
.team-photo{position:absolute;left:620px;top:67px;width:491px;height:368px;border-radius:10px;background:linear-gradient(135deg,#6f7275,#3a3c3f 55%,#1b1c1e)}

/* cta */
.cta{position:absolute;top:2081px;left:0;width:1200px;height:309px;text-align:center}
.cta h2{position:absolute;top:52px;width:1200px;font-size:40px;line-height:41px}
.cta p{position:absolute;top:149px;width:1200px;font-size:11.5px;color:var(--muted)}
.cta .btn{position:absolute;left:520px;top:187px;width:155px;height:34px;font-size:11px}

/* footer */
.site-footer{position:absolute;top:2390px;left:0;width:1200px;height:323px;background:var(--bg-footer)}
.footer-brand{position:absolute;left:27px;top:40px}
.footer-about{position:absolute;left:27px;top:92px;font-size:11.5px;line-height:19px;color:var(--muted)}
.socials{position:absolute;left:27px;top:138px;display:flex;gap:10px}
.socials a{height:26px;padding:0 8px;border:1px solid #232633;border-radius:6px;background:#161a25;display:flex;align-items:center;font-size:9px;color:var(--muted)}
.footer-col{position:absolute;top:49px}
.footer-col h4{font-family:"JetBrains Mono",monospace;font-weight:500;font-size:8.5px;letter-spacing:1px;color:var(--dim)}
.footer-col ul{list-style:none;margin-top:12px}
.footer-col li{font-size:9.5px;color:var(--muted);height:25px}
.footer-bottom{position:absolute;top:270px;left:27px;width:1141px;display:flex;justify-content:space-between;font-size:9.5px;color:var(--muted)}
</style>
</head>
<body>

<header class="site-header">
  <a class="brand" href="#"><span class="brand-mark"></span><span class="brand-name">Trelvo</span></a>
  <nav class="main-nav">
    <a href="#">Services</a><a class="active" href="#">Solutions</a><a href="#">Company</a><a href="#">Contact</a>
  </nav>
  <div class="lang">
    <svg width="11" height="11" viewBox="0 0 24 24" fill="none" stroke="currentColor" stroke-width="2"><circle cx="12" cy="12" r="10"/><path d="M2 12h20M12 2a15 15 0 010 20M12 2a15 15 0 000 20"/></svg>EN
  </div>
  <a class="btn header-cta" href="#">Book a call</a>
</header>

<section class="hero grid-bg">
  <div class="eyebrow hero-label">SOLUTIONS</div>
  <h1 class="display hero-title">Tailored Solutions</h1>
  <p class="hero-lead">We don't believe in one-size-fits-all. Our solutions are designed around your business needs, technical requirements, and growth ambitions.</p>

  <div class="solutions">
    <article class="solution-card">
      <div class="icon-box"><svg width="17" height="17" viewBox="0 0 24 24" fill="none" stroke="#82ff00" stroke-width="2"><rect x="4" y="3" width="16" height="18" rx="2"/><path d="M9 21v-4h6v4M8 7h2M14 7h2M8 11h2M14 11h2"/></svg></div>
      <h3>Data Center Modernization</h3>
      <p>Transform your on-premises infrastructure with modern virtualization, storage, and backup solutions.</p>
      <ul class="checks">
        <li><svg width="12" height="12" viewBox="0 0 24 24" fill="none" stroke="#82ff00" stroke-width="2.2"><circle cx="12" cy="12" r="10"/><path d="M8 12l3 3 5-6"/></svg>Nexorin &amp; Quadr-X virtualization</li>
        <li><svg width="12" height="12" viewBox="0 0 24 24" fill="none" stroke="#82ff00" stroke-width="2.2"><circle cx="12" cy="12" r="10"/><path d="M8 12l3 3 5-6"/></svg>Software-defined storage</li>
        <li><svg width="12" height="12" viewBox="0 0 24 24" fill="none" stroke="#82ff00" stroke-width="2.2"><circle cx="12" cy="12" r="10"/><path d="M8 12l3 3 5-6"/></svg>Backup &amp; disaster recovery</li>
        <li><svg width="12" height="12" viewBox="0 0 24 24" fill="none" stroke="#82ff00" stroke-width="2.2"><circle cx="12" cy="12" r="10"/><path d="M8 12l3 3 5-6"/></svg>Infrastructure automation</li>
      </ul>
      <a class="outline-btn" href="#">Discuss your needs <span>→</span></a>
    </article>

    <article class="solution-card">
      <div class="icon-box cloud"><svg width="17" height="17" viewBox="0 0 24 24" fill="none" stroke="#82ff00" stroke-width="2"><path d="M17.5 19H9a7 7 0 116.7-9h1.8a4.5 4.5 0 010 9z"/></svg></div>
      <h3>Cloud &amp; Hybrid</h3>
      <p>Leverage the cloud while maintaining control. We design hybrid architectures that balance flexibility with compliance.</p>
      <ul class="checks">
        <li><svg width="12" height="12" viewBox="0 0 24 24" fill="none" stroke="#82ff00" stroke-width="2.2"><circle cx="12" cy="12" r="10"/><path d="M8 12l3 3 5-6"/></svg>Nimbra &amp; Cloudex migration</li>
        <li><svg width="12" height="12" viewBox="0 0 24 24" fill="none" stroke="#82ff00" stroke-width="2.2"><circle cx="12" cy="12" r="10"/><path d="M8 12l3 3 5-6"/></svg>Hybrid connectivity</li>
        <li><svg width="12" height="12" viewBox="0 0 24 24" fill="none" stroke="#82ff00" stroke-width="2.2"><circle cx="12" cy="12" r="10"/><path d="M8 12l3 3 5-6"/></svg>Cloud cost optimization</li>
        <li><svg width="12" height="12" viewBox="0 0 24 24" fill="none" stroke="#82ff00" stroke-width="2.2"><circle cx="12" cy="12" r="10"/><path d="M8 12l3 3 5-6"/></svg>Multi-cloud management</li>
      </ul>
      <a class="outline-btn" href="#">Discuss your needs <span>→</span></a>
    </article>

    <article class="solution-card">
      <div class="icon-box swap"><svg width="17" height="17" viewBox="0 0 24 24" fill="none" stroke="#82ff00" stroke-width="2"><path d="M16 3l4 4-4 4M20 7H4M8 21l-4-4 4-4M4 17h16"/></svg></div>
      <h3>Migration &amp; Transformation</h3>
      <p>Move from legacy to modern with confidence. Our proven methodology minimizes risk and downtime.</p>
      <ul class="checks">
        <li><svg width="12" height="12" viewBox="0 0 24 24" fill="none" stroke="#82ff00" stroke-width="2.2"><circle cx="12" cy="12" r="10"/><path d="M8 12l3 3 5-6"/></svg>Application migration</li>
        <li><svg width="12" height="12" viewBox="0 0 24 24" fill="none" stroke="#82ff00" stroke-width="2.2"><circle cx="12" cy="12" r="10"/><path d="M8 12l3 3 5-6"/></svg>Data center relocation</li>
        <li><svg width="12" height="12" viewBox="0 0 24 24" fill="none" stroke="#82ff00" stroke-width="2.2"><circle cx="12" cy="12" r="10"/><path d="M8 12l3 3 5-6"/></svg>Platform upgrades</li>
        <li><svg width="12" height="12" viewBox="0 0 24 24" fill="none" stroke="#82ff00" stroke-width="2.2"><circle cx="12" cy="12" r="10"/><path d="M8 12l3 3 5-6"/></svg>End-user migration</li>
      </ul>
      <a class="outline-btn" href="#">Discuss your needs <span>→</span></a>
    </article>

    <article class="solution-card">
      <div class="icon-box shield"><svg width="17" height="17" viewBox="0 0 24 24" fill="none" stroke="#82ff00" stroke-width="2"><path d="M12 2l8 3v6c0 5-3.5 9-8 11-4.5-2-8-6-8-11V5z"/><path d="M9 12l2 2 4-4"/></svg></div>
      <h3>Security &amp; Zero Trust</h3>
      <p>Protect your assets with modern security frameworks. Identity-first, always-verified, never-trusted.</p>
      <ul class="checks">
        <li><svg width="12" height="12" viewBox="0 0 24 24" fill="none" stroke="#82ff00" stroke-width="2.2"><circle cx="12" cy="12" r="10"/><path d="M8 12l3 3 5-6"/></svg>Identity &amp; access management</li>
        <li><svg width="12" height="12" viewBox="0 0 24 24" fill="none" stroke="#82ff00" stroke-width="2.2"><circle cx="12" cy="12" r="10"/><path d="M8 12l3 3 5-6"/></svg>Conditional access policies</li>
        <li><svg width="12" height="12" viewBox="0 0 24 24" fill="none" stroke="#82ff00" stroke-width="2.2"><circle cx="12" cy="12" r="10"/><path d="M8 12l3 3 5-6"/></svg>Endpoint protection</li>
        <li><svg width="12" height="12" viewBox="0 0 24 24" fill="none" stroke="#82ff00" stroke-width="2.2"><circle cx="12" cy="12" r="10"/><path d="M8 12l3 3 5-6"/></svg>Security monitoring</li>
      </ul>
      <a class="outline-btn" href="#">Discuss your needs <span>→</span></a>
    </article>
  </div>
</section>

<section class="approach grid-bg">
  <div class="eyebrow">OUR APPROACH</div>
  <h2 class="display">How We Work</h2>
  <div class="steps">
    <div class="step"><div class="step-num">01</div><h3>Discover</h3><p>We assess your current state, understand your goals, and identify opportunities.</p></div>
    <div class="step"><div class="step-num">02</div><h3>Design</h3><p>We architect solutions tailored to your needs, with clear roadmaps and timelines.</p></div>
    <div class="step"><div class="step-num">03</div><h3>Deliver</h3><p>We implement with precision, keeping you informed at every step.</p></div>
    <div class="step"><div class="step-num">04</div><h3>Operate</h3><p>We provide ongoing support and optimization to ensure long-term success.</p></div>
  </div>
</section>

<section class="industries">
  <div class="eyebrow">INDUSTRIES</div>
  <h2 class="display">Who We Serve</h2>
  <p class="lead">We work with organizations across industries, bringing deep expertise and proven methodologies to every engagement.</p>
  <div class="industry-list">
    <div class="chip"><svg width="11" height="11" viewBox="0 0 24 24" fill="none" stroke="#82ff00" stroke-width="2.2"><circle cx="12" cy="12" r="10"/><path d="M8 12l3 3 5-6"/></svg>Manufacturing</div>
    <div class="chip"><svg width="11" height="11" viewBox="0 0 24 24" fill="none" stroke="#82ff00" stroke-width="2.2"><circle cx="12" cy="12" r="10"/><path d="M8 12l3 3 5-6"/></svg>Logistics</div>
    <div class="chip"><svg width="11" height="11" viewBox="0 0 24 24" fill="none" stroke="#82ff00" stroke-width="2.2"><circle cx="12" cy="12" r="10"/><path d="M8 12l3 3 5-6"/></svg>Healthcare</div>
    <div class="chip"><svg width="11" height="11" viewBox="0 0 24 24" fill="none" stroke="#82ff00" stroke-width="2.2"><circle cx="12" cy="12" r="10"/><path d="M8 12l3 3 5-6"/></svg>Finance</div>
    <div class="chip"><svg width="11" height="11" viewBox="0 0 24 24" fill="none" stroke="#82ff00" stroke-width="2.2"><circle cx="12" cy="12" r="10"/><path d="M8 12l3 3 5-6"/></svg>Retail</div>
    <div class="chip"><svg width="11" height="11" viewBox="0 0 24 24" fill="none" stroke="#82ff00" stroke-width="2.2"><circle cx="12" cy="12" r="10"/><path d="M8 12l3 3 5-6"/></svg>Technology</div>
  </div>
  <div class="team-photo" role="img" aria-label="Black and white photo of a consulting team meeting around a conference table in front of a presentation screen"></div>
</section>

<section class="cta">
  <h2 class="display">Ready to start your<br>project?</h2>
  <p>Let's discuss your challenges and design a solution that fits your business.</p>
  <a class="btn" href="#"><svg width="11" height="11" viewBox="0 0 24 24" fill="none" stroke="currentColor" stroke-width="2.2"><rect x="3" y="5" width="18" height="16" rx="2"/><path d="M3 10h18M8 3v4M16 3v4"/></svg>Book a consultation</a>
</section>

<footer class="site-footer">
  <a class="brand footer-brand" href="#"><span class="brand-mark"></span><span class="brand-name" style="font-size:19px">Trelvo</span></a>
  <p class="footer-about">IT consulting and managed services.<br>Based in Germany, serving Europe.</p>
  <div class="socials"><a href="#">Brumble</a><a href="#">Chirply</a><a href="#">Info</a></div>
  <div class="footer-col" style="left:324px"><h4>SERVICES</h4><ul><li>Managed Services</li><li>Cloud &amp; Hybrid</li><li>Modern Workplace</li><li>Security</li><li>Network</li><li>Data Center</li></ul></div>
  <div class="footer-col" style="left:620px"><h4>COMPANY</h4><ul><li>About Us</li><li>Careers</li><li>References</li><li>Partners</li><li>Contact</li></ul></div>
  <div class="footer-col" style="left:916px"><h4>LEGAL</h4><ul><li>Imprint</li><li>Privacy Policy</li><li>Terms of Service</li><li>Data Protection</li></ul></div>
  <div class="footer-bottom"><span>© 2026 Trelvo UG. All rights reserved.</span><span>Made with precision in Germany</span></div>
</footer>

</body>
</html>
```